Website for Fernvale Harmony Chapel

Wordpress website design required for Fernvale Harmony Chapel. We are a family oriented church catering for age groups from school age to elderly people. The church has a wide variety of activities which it coordinates. The idea is to describe the activities on the activities page, but cross-link them to show which would be applicable to the different age groups.

We would like an inviting website which is easy to read and navigate.

Target Market(s)

Very wide audience - from school age youth to elderly people, so design and style should cater for both audiences.

Industry/Entity Type

Church

Coding

Coded - Design and coding required

Number of Pages Required

5+ page

Font styles to use
Sans Serif

Colors
0255a3
ffffff
0792cd
f78f20

Requirements
Must have
• Inviting website.
• Clear readable font.
• Space to import photos to balance text on each page.
• Need to project a dynamic and progressive feel for the church.
• Easy to navigate.
Nice to have
• Scrolling photos on pages. Ability to enter questions/ comments/prayer requests on Home page.
Should not have
• Conservative audience, so should not be too bold.

```html
<!DOCTYPE html>
<html lang="en">
<head>
<meta charset="utf-8">
<title>Fernvale Harmony Chapel</title>
<link href="https://fonts.googleapis.com/css2?family=Gelasio:ital,wght@0,400;0,700;1,400&family=Open+Sans:wght@400;600&family=Raleway:wght@700&display=swap" rel="stylesheet">
<style>
:root{
  --navy:#0c2753;
  --navy-deep:#0a2450;
  --gold:#8a7537;
  --ink:#222;
  --text:#3a3a3a;
  --band:#262626;
  --footer:#151515;
  --footer-line:#2a2a2a;
  --footer-text:#8d8d8d;
  --white:#fff;
}
*{margin:0;padding:0;box-sizing:border-box}
html,body{width:1200px;height:2446px;overflow:hidden;background:var(--white)}
body{position:relative;font-family:"Gelasio",Georgia,serif;color:var(--ink)}
.abs{position:absolute}

/* header */
.brand{left:98px;top:92px;display:flex;align-items:center;gap:8px}
.brand-dot{width:16px;height:16px;border-radius:50%;background:var(--navy)}
.brand-name{font-size:25px;color:var(--navy);font-weight:400;letter-spacing:.2px}
.utility{right:200px;top:46px;font-size:14px;font-style:italic;color:#333;word-spacing:4px}
.utility span{margin:0 14px}
.nav{right:98px;top:104px;display:flex;font-size:14px}
.nav a{color:#333;text-decoration:none;padding:5px 14px;margin-left:16px}
.nav a.active{background:var(--navy);color:var(--white)}

/* hero */
.hero{left:0;top:150px;width:1200px;height:508px;background:linear-gradient(180deg,#8fb3d9 0%,#b9a88a 45%,#7a6a55 100%)}
.hero-caption{left:98px;top:505px;font-size:26px;color:var(--white);line-height:40px}
.hero-caption span{display:inline-block;background:rgba(12,39,83,.75);padding:0 8px;margin-bottom:2px}
.hero-caption span.alt{background:rgba(138,117,55,.8)}
.dots{left:570px;top:622px;display:flex;gap:8px}
.dots i{width:7px;height:7px;border-radius:50%;background:rgba(255,255,255,.5)}
.dots i:first-child{background:var(--white)}

/* section titles */
.title{font-size:32px;font-weight:400;color:var(--ink)}
.center{left:0;width:1200px;text-align:center}
.lede{left:98px;width:1004px;text-align:center;font-size:13px;line-height:20px;color:var(--text)}
.btn{display:block;text-align:center;color:var(--white);font-size:14px}
.btn-navy{background:var(--navy)}
.btn-gold{background:var(--gold)}

/* gallery */
.gallery{left:98px;top:992px;display:flex;gap:17px}
.gallery-item{width:238px}
.gallery-photo{height:176px}
.gallery-cap{margin-top:10px;font-size:14px;line-height:18px;color:var(--ink)}

/* message */
.message{left:0;top:1265px;width:1200px;height:217px;background:var(--band)}
.message .title{color:var(--white)}
.message-text{left:98px;width:1004px;top:82px;text-align:center;color:var(--white);font-size:12px;line-height:18px;font-weight:700}

/* news */
.news{left:98px;top:1585px;display:flex;gap:26px}
.news-card{width:230px;height:248px;border:1px solid #e3e3e3;position:relative;background:var(--white)}
.news-photo{height:133px;position:relative}
.news-date{position:absolute;left:12px;top:12px;width:36px;height:34px;background:#1b1b1b;color:var(--white);font-family:"Open Sans",sans-serif;font-size:8px;text-align:center;line-height:10px;padding-top:7px}
.news-title{font-family:"Raleway",sans-serif;font-size:13px;font-weight:700;margin:20px 9px 10px}
.news-body{font-family:"Open Sans",sans-serif;font-size:9.6px;line-height:21px;color:#666;margin:0 9px;letter-spacing:-.1px}
.news-body b{color:#2b79c2;font-weight:600}

/* prayer */
.prayer{left:0;top:1893px;width:1200px;height:180px;background:var(--navy-deep)}
.prayer-title{left:98px;top:48px;font-size:30px;color:var(--white);font-weight:400}
.prayer-text{left:98px;top:90px;width:680px;font-size:12px;line-height:19px;color:var(--white);font-weight:700}
.prayer-btn{left:805px;top:68px;width:231px;height:53px;line-height:53px;font-size:16px;box-shadow:0 3px 0 #5e4f22}

/* footer */
.footer{left:0;top:2073px;width:1200px;height:373px;background:var(--footer);font-family:"Open Sans",sans-serif}
.f-head{top:45px;font-size:11.5px;color:var(--gold);letter-spacing:.6px;font-weight:400}
.f-text{font-size:13px;line-height:20px;color:var(--footer-text)}
.f-contact{left:600px;width:235px}
.f-row{display:flex;gap:14px;align-items:flex-start;font-size:12px;color:#bbb;line-height:20px;padding:10px 0;border-bottom:1px solid var(--footer-line)}
.f-row svg{flex:none;margin-top:4px}
.f-field{left:872px;width:229px;background:#222;font-size:9.5px;color:#ddd;padding:6px 8px}
.send{left:975px;top:252px;width:126px;height:28px;line-height:28px;font-size:9.5px}
.copyright{left:98px;top:330px;font-size:10.5px;color:#ddd}
.copyright em{font-style:normal;color:var(--gold)}
.social{left:1012px;top:329px;display:flex;gap:17px}
.social i{width:14px;height:14px;background:#777;border-radius:2px}
</style>
</head>
<body>

<header>
  <div class="abs brand"><span class="brand-dot"></span><span class="brand-name">Fernvale Harmony Chapel</span></div>
  <div class="abs utility">Enter questions <span>/</span> Comments</div>
  <nav class="abs nav">
    <a class="active">Home</a><a>Age Group</a><a>Activites</a><a>Event Calendar</a><a>About</a><a>Contact</a>
  </nav>
</header>

<section class="abs hero" role="img" aria-label="Photo of a stone church on a sunny village square with café umbrellas"></section>
<div class="abs hero-caption">
  <span>We are a family oriented church catering for age groups</span><br>
  <span class="alt">from school age to elderly people</span>
</div>
<div class="abs dots"><i></i><i></i><i></i><i></i></div>

<h2 class="abs title center" style="top:688px">Welcome To Our Site</h2>
<p class="abs lede" style="top:745px">Donec eros erat, ultricies et commodo in, viverra sit amet orci. Etiam commodo tempor erat, a gravida metus porta et. Etiam mattis in ligula quis condimentum. Nunc varius lectus nibh, eget porttitor augue posuere non. In aliquet purus lorem, sit amet volutpat lorem auctor nec. Donec pharetra et massa sed pretium. Aenean vel molestie leo, vel aliquet nunc. Maecenas semper sodales tortor, sit amet congue ipsum gravida ac. Cras congue malesuada turpis id fermentum. Nulla a arcu ac nulla laoreet lobortis volutpat et nibh. Aliquam blandit venenatis odio. Aliquam at urna pellentesque, cursus mi nec, tincidunt tortor. Nunc pulvinar cursus tempor. Maecenas sit amet ullamcorper elit. In porta lorem leo, quis varius metus tincidunt aliquam. Nulla maximus sed erat eget suscipit.</p>
<a class="abs btn btn-navy" style="left:539px;top:869px;width:118px;height:32px;line-height:32px">Read More</a>

<h2 class="abs title" style="left:98px;top:928px">Our Gallery</h2>
<svg class="abs" style="left:1056px;top:940px" width="46" height="22" viewBox="0 0 46 22">
  <circle cx="11" cy="11" r="10" fill="#8a7537"/><path d="M13 6l-5 5 5 5" stroke="#fff" stroke-width="2" fill="none"/>
  <circle cx="35" cy="11" r="10" fill="#9a9a9a"/><path d="M33 6l5 5-5 5" stroke="#fff" stroke-width="2" fill="none"/>
</svg>
<div class="abs gallery">
  <figure class="gallery-item"><div class="gallery-photo" role="img" aria-label="Ornate church altar with a statue in a blue niche" style="background:linear-gradient(135deg,#2d3f7a,#8a6a3a)"></div><figcaption class="gallery-cap">finibus ipsum. Curabitur in magna at erat sollicitudin maximus</figcaption></figure>
  <figure class="gallery-item"><div class="gallery-photo" role="img" aria-label="Town square with a fountain and historic buildings" style="background:linear-gradient(180deg,#4f86d0,#c79a6a 60%,#8a7a66)"></div><figcaption class="gallery-cap">finibus ipsum. Curabitur in magna at erat sollicitudin maximus</figcaption></figure>
  <figure class="gallery-item"><div class="gallery-photo" role="img" aria-label="White candles on a table by a bright window" style="background:linear-gradient(180deg,#e8e6e0,#c8c3b8 70%,#8fa07a)"></div><figcaption class="gallery-cap">finibus ipsum. Curabitur in magna at erat sollicitudin maximus</figcaption></figure>
  <figure class="gallery-item"><div class="gallery-photo" role="img" aria-label="Plates of food served at a shared meal" style="background:linear-gradient(135deg,#c23a2a,#e8e2d8 55%,#c9a24a)"></div><figcaption class="gallery-cap">finibus ipsum. Curabitur in magna at erat sollicitudin maximus</figcaption></figure>
</div>

<section class="abs message">
  <h2 class="abs title center" style="top:28px">Message</h2>
  <p class="abs message-text">Donec eros erat, ultricies et commodo in, viverra sit amet orci. Etiam commodo tempor erat, a gravida metus porta et. Etiam mattis in ligula quis condimentum. Nunc varius lectus nibh, eget porttitor augue posuere non. In aliquet purus lorem, sit amet volutpat lorem auctor nec. Donec pharetra et massa sed pretium. Aenean vel molestie leo, vel aliquet nunc. Maecenas semper sodales tortor, sit amet congue ipsum gravida ac. Cras congue malesuada turpis id fermentum.</p>
  <a class="abs btn btn-gold" style="left:539px;top:153px;width:118px;height:32px;line-height:32px">View All</a>
</section>

<h2 class="abs title center" style="top:1510px">News</h2>
<div class="abs news">
  <article class="news-card"><div class="news-photo" role="img" aria-label="Twin church spires against a blue sky" style="background:linear-gradient(180deg,#3f7fd0,#6f9a6a 70%,#5a5a5a)"><div class="news-date">17<br>MAR</div></div><h3 class="news-title">Blog Post Title Here</h3><p class="news-body">It is a long established fact that a reader will be distracted by the readable content of a page when looking at its layout. <b>Read More</b></p></article>
  <article class="news-card"><div class="news-photo" role="img" aria-label="Banquet table set with white linen" style="background:linear-gradient(135deg,#c9b9a0,#f1ece4)"><div class="news-date">10<br>MAR</div></div><h3 class="news-title">Blog Post Title Here</h3><p class="news-body">It is a long established fact that a reader will be distracted by the readable content of a page when looking at its layout. <b>Read More</b></p></article>
  <article class="news-card"><div class="news-photo" role="img" aria-label="White flower arrangement on a table" style="background:linear-gradient(135deg,#b8a27a,#f3eee6 60%,#d9cdb8)"><div class="news-date">12<br>FEB</div></div><h3 class="news-title">Blog Post Title Here</h3><p class="news-body">It is a long established fact that a reader will be distracted by the readable content of a page when looking at its layout. <b>Read More</b></p></article>
  <article class="news-card"><div class="news-photo" role="img" aria-label="Terrace table overlooking a lake and hills" style="background:linear-gradient(180deg,#5f8fc8,#6c8a7a 55%,#e6e6e6)"><div class="news-date">29<br>JAN</div></div><h3 class="news-title">Blog Post Title Here</h3><p class="news-body">It is a long established fact that a reader will be distracted by the readable content of a page when looking at its layout. <b>Read More</b></p></article>
</div>

<section class="abs prayer">
  <h2 class="abs prayer-title">Prayer request</h2>
  <p class="abs prayer-text">Donec eros erat, ultricies et commodo in, viverra sit amet orci. Etiam commodo tempor erat, a gravida metus porta et.<br>Etiam mattis in ligula quis condimentum.</p>
  <a class="abs btn btn-gold prayer-btn">REQUEST NOW</a>
</section>

<footer class="abs footer">
  <h4 class="abs f-head" style="left:98px">OUR MISSION</h4>
  <p class="abs f-text" style="left:98px;top:90px;width:262px">Lorem ipsum dolor sit amet, consectetur adipi-scing elit. Nulla sodales, odio id dapibus pulvi-nar, augue risus efficitur ipsum, at venenatis dolor dui et leo. Praesent vulputate quis erat quis finibus.</p>
  <p class="abs f-text" style="left:98px;top:200px;font-size:12px;color:#555">Read More &gt;&gt;</p>

  <h4 class="abs f-head" style="left:405px">SERVICE TIMES</h4>
  <p class="abs f-text" style="left:405px;top:90px">Monday to Saturday<br>9AM &nbsp;- &nbsp; 6PM</p>
  <p class="abs f-text" style="left:405px;top:138px">Sunday<br>Holiday</p>

  <h4 class="abs f-head" style="left:600px">CONTACT INFO</h4>
  <div class="abs f-contact" style="top:82px">
    <div class="f-row"><svg width="14" height="11" viewBox="0 0 14 11"><rect x="1" y="1" width="12" height="9" fill="none" stroke="#ccc" stroke-width="1.4"/><path d="M1 1l6 5 6-5" fill="none" stroke="#ccc" stroke-width="1.4"/></svg>info@domain.com</div>
    <div class="f-row"><svg width="14" height="13" viewBox="0 0 14 14"><path d="M3 1l3 3-1.5 2c1 2 2 3 3.5 3.5L10 8l3 3-2 2C6 12 2 8 1 3z" fill="#ccc"/></svg>(800) 555-0147</div>
    <div class="f-row" style="border:0"><svg width="14" height="14" viewBox="0 0 14 14"><path d="M7 1a4 4 0 0 1 4 4c0 3-4 8-4 8S3 8 3 5a4 4 0 0 1 4-4z" fill="#ccc"/><circle cx="7" cy="5" r="1.5" fill="#151515"/></svg>48 Willow Lane, Suite 12<br>Fernvale, FL 33099</div>
  </div>

  <h4 class="abs f-head" style="left:872px">CONTACT US</h4>
  <div class="abs f-field" style="top:90px;height:27px">Name</div>
  <div class="abs f-field" style="top:123px;height:27px">Email Address</div>
  <div class="abs f-field" style="top:156px;height:66px">Message</div>
  <a class="abs btn btn-gold send">SEND</a>

  <p class="abs copyright">Copyright © 2016 - <em>yoursite</em>, All Rights Reserved</p>
  <div class="abs social" aria-label="Social links"><i></i><i></i><i></i></div>
</footer>

</body>
</html>
```